Sationery for a dental office
Brisk Dental
Project: Sationery for a dental office
Sationery for a dental office - Health
Creative Brief
Professional
Dr Nuvela Pritch
XXXX- be provided later
briskdentalqz@mailnest.example
www.briskhomedental.example
The phone number, email address, website address and address fields need to be included but should all be able to be edited it the final versions of all the stationery. Along with business name: Brisk Dental also include slogan and tagline: tagline: Family, cosmetic & Implant Dentistry slogan: A healthy body begins with a healthy mouth
One version of the business card should have an appointment card layout on the back, which has section for day, date, time to be filled in. Another version: just logo, slogan and tagline on one side of the card and the other side having, doctor's name, address, phone number, website address, email address Again all these fields need to be easily edited in the final version.

```html
<!DOCTYPE html>
<html lang="en">
<head>
<meta charset="utf-8">
<title>Brisk Dental – Business Card</title>
<link rel="stylesheet" href="https://fonts.googleapis.com/css2?family=Questrial&display=swap">
<style>
  :root {
    --bg: #e9ebee;
    --card: #ffffff;
    --teal: #1f7f76;
    --teal-dark: #16615c;
    --blue: #1d6fb8;
    --blue-light: #5fb3e6;
    --navy: #1c3f7a;
    --ink: #3a3a3a;
    --muted: #666666;
    --rule: #8a8a8a;
  }
  * { box-sizing: border-box; margin: 0; padding: 0; }
  html, body { width: 1200px; height: 901px; overflow: hidden; }
  body {
    background: var(--bg);
    font-family: "Questrial", "Century Gothic", sans-serif;
    color: var(--ink);
    position: relative;
  }
  .card {
    position: absolute;
    top: 295px;
    width: 540px;
    height: 310px;
    background: var(--card);
    box-shadow: 0 6px 18px rgba(0,0,0,0.18);
    overflow: hidden;
  }
  .card--front { left: 40px; }
  .card--back { left: 620px; }

  .wave { position: absolute; inset: 0; width: 100%; height: 100%; }

  .brand {
    position: absolute;
    top: 28px;
    right: 26px;
    text-align: right;
  }
  .brand__row { display: flex; align-items: center; justify-content: flex-end; gap: 8px; }
  .brand__dot { width: 30px; height: 30px; border-radius: 50%; background: var(--navy); }
  .brand__name { font-size: 29px; color: var(--blue); letter-spacing: 1px; line-height: 1; }
  .brand__tagline { font-size: 10px; color: var(--muted); margin-top: 4px; }
  .brand__slogan { font-size: 10px; color: var(--muted); font-style: italic; margin-top: 1px; }

  .doctor {
    position: absolute;
    top: 126px;
    left: 300px;
    width: 170px;
    text-align: center;
  }
  .doctor__name { font-size: 15px; color: var(--blue); }
  .doctor__title { font-size: 9px; color: var(--muted); margin-top: 2px; }

  .contact {
    position: absolute;
    left: 18px;
    top: 172px;
    color: #ffffff;
    font-size: 10.5px;
    line-height: 1.45;
    list-style: none;
  }
  .contact li { display: flex; align-items: center; gap: 5px; }
  .contact svg { width: 9px; height: 9px; flex: none; }

  .appt {
    position: absolute;
    inset: 0;
    padding: 0 58px;
  }
  .appt__rule { position: absolute; height: 1px; background: var(--rule); }
  .appt__heading {
    position: absolute;
    top: 42px; left: 0; right: 0;
    text-align: center;
    font-size: 15px;
    color: var(--ink);
  }
  .appt__labels {
    position: absolute;
    top: 100px; left: 58px; right: 58px;
    display: flex;
    justify-content: space-between;
    font-size: 14px;
  }
  .appt__time {
    position: absolute;
    top: 152px; left: 58px; right: 58px;
    display: flex;
    align-items: flex-end;
    font-size: 14px;
    gap: 8px;
  }
  .appt__blank { flex: 1; border-bottom: 1px solid var(--rule); height: 12px; }
  .appt__note {
    position: absolute;
    top: 198px; left: 0; right: 0;
    text-align: center;
    font-size: 10.5px;
    font-style: italic;
    color: var(--muted);
  }
  .appt__web {
    position: absolute;
    top: 250px; left: 0; right: 0;
    display: flex; justify-content: center; align-items: center; gap: 6px;
    font-size: 10px;
    color: var(--ink);
  }
  .appt__web-dot { width: 11px; height: 11px; border-radius: 50%; background: var(--navy); }
</style>
</head>
<body>

<section class="card card--front" aria-label="Business card front">
  <svg class="wave" viewBox="0 0 540 310" preserveAspectRatio="none" aria-hidden="true">
    <path d="M0,30 C140,45 240,120 320,215 C355,258 390,290 430,310 L0,310 Z" fill="#5fb3e6"/>
    <path d="M0,40 C135,58 232,130 308,222 C340,262 372,292 405,310 L0,310 Z" fill="#1d6fb8"/>
    <path d="M0,48 C130,66 224,138 298,228 C328,266 355,292 385,310 L0,310 Z" fill="#ffffff"/>
    <path d="M0,54 C125,72 216,145 288,232 C316,268 340,294 368,310 L0,310 Z" fill="#1c3f7a"/>
    <path d="M0,60 C120,80 208,152 278,238 C304,272 326,296 352,310 L0,310 Z" fill="#1f7f76"/>
    <path d="M0,150 C90,150 170,200 230,310 L0,310 Z" fill="#16615c" opacity="0.35"/>
  </svg>

  <div class="brand">
    <div class="brand__row">
      <span class="brand__dot"></span>
      <span class="brand__name">Brisk Dental</span>
    </div>
    <p class="brand__tagline">Family, Cosmetic &amp; Implant Dentistry</p>
    <p class="brand__slogan">A healthy body begins with a healthy mouth</p>
  </div>

  <div class="doctor">
    <p class="doctor__name">Dr Nuvela Pritch</p>
    <p class="doctor__title">Your Title</p>
  </div>

  <ul class="contact">
    <li>2840 Marlow Lane</li>
    <li>Unit 106</li>
    <li>Fernbrook, WI 53000</li>
    <li><svg viewBox="0 0 10 10"><path d="M2,1 L4,1 L4.6,3 L3.5,4 C4,5.3 4.7,6 6,6.5 L7,5.4 L9,6 L9,8 C5,8.5 1.5,5 2,1 Z" fill="#fff"/></svg>262-555-0148</li>
    <li><svg viewBox="0 0 10 10"><path d="M2,1 L4,1 L4.6,3 L3.5,4 C4,5.3 4.7,6 6,6.5 L7,5.4 L9,6 L9,8 C5,8.5 1.5,5 2,1 Z" fill="#fff"/></svg>262-555-0193</li>
    <li><svg viewBox="0 0 10 10"><rect x="1" y="2" width="8" height="6" fill="none" stroke="#fff"/><path d="M1,2 L5,5.5 L9,2" fill="none" stroke="#fff"/></svg>briskdentalqz@mailnest.example</li>
    <li>www.briskhomedental.example</li>
  </ul>
</section>

<section class="card card--back" aria-label="Appointment card back">
  <div class="appt">
    <span class="appt__rule" style="top:30px;left:150px;right:150px;"></span>
    <p class="appt__heading">Has An Appointment On</p>
    <span class="appt__rule" style="top:72px;left:58px;right:58px;"></span>
    <div class="appt__labels">
      <span>Day</span><span>Month</span><span>Date</span>
    </div>
    <div class="appt__time">
      <span>At</span><span class="appt__blank"></span>
      <span>AM</span><span class="appt__blank"></span>
      <span>PM</span>
    </div>
    <p class="appt__note">If unable to keep appointment, kindly give 24 hrs. notice</p>
    <p class="appt__web"><span class="appt__web-dot"></span>www.briskhomedental.example</p>
  </div>
</section>

</body>
</html>
```